Quarry Vale Business Cards

We need to design some upbeat business cards. We are an Industrial Rope Access Company/Height Safety Company that specialize in Rope Access, Confined Space, Anchor Points, Safety Systems, PPE Inspecions and Rigging.
Company name is Quarry Vale Ltd
Card is for Reggie Stanton the Company Director
His mobile number is 027 816 4920 and email is reggie@quarryvale.co.nz. Website address is www.quarryvale.co.nz.
We will post some pictures below to ensure you get a good idea of what we do.

```html
<!DOCTYPE html>
<html lang="en">
<head>
<meta charset="utf-8">
<title>Quarry Vale Business Cards</title>
<link rel="stylesheet" href="https://fonts.googleapis.com/css2?family=Lato:wght@400;700;900&display=swap">
<style>
  :root {
    --backdrop: #4a4a4e;
    --card: #141416;
    --card-edge: #1d1d20;
    --silver: #c9cacd;
    --text: #b8b9bc;
    --accent: #3b5bff;
  }
  html, body {
    margin: 0;
    width: 1200px;
    height: 1000px;
    overflow: hidden;
    background: var(--backdrop);
    font-family: "Lato", sans-serif;
  }
  .stage {
    position: relative;
    width: 1200px;
    height: 1000px;
  }
  .card {
    position: absolute;
    left: 250px;
    width: 700px;
    height: 400px;
    border-radius: 22px;
    background: linear-gradient(160deg, var(--card-edge), var(--card));
    box-shadow: 0 18px 40px rgba(0,0,0,0.45);
    overflow: hidden;
  }
  .card--front { top: 70px; }
  .card--back { top: 530px; }
  .brand {
    position: absolute;
    top: 40px;
    right: 46px;
    margin: 0;
    font-weight: 900;
    font-size: 58px;
    letter-spacing: 1px;
    color: var(--silver);
  }
  .services {
    position: absolute;
    margin: 0;
    padding: 0;
    list-style: none;
    font-size: 18px;
    color: var(--text);
  }
  .services li {
    position: relative;
    padding-left: 16px;
    line-height: 26px;
  }
  .services li::before {
    content: "";
    position: absolute;
    left: 0;
    top: 10px;
    width: 6px;
    height: 6px;
    background: var(--accent);
  }
  .services--main { left: 70px; top: 150px; }
  .services--extra { left: 440px; top: 190px; }
  .site {
    position: absolute;
    left: 0;
    right: 0;
    bottom: 48px;
    text-align: center;
    font-size: 19px;
    font-weight: 700;
    color: var(--text);
    letter-spacing: 0.5px;
  }
  .site .domain { color: var(--accent); }
  .contact-block {
    position: absolute;
    left: 46px;
    right: 46px;
    bottom: 48px;
  }
  .person {
    font-size: 22px;
    color: var(--silver);
    text-transform: uppercase;
    letter-spacing: 0.5px;
  }
  .person .role {
    font-size: 17px;
    color: var(--accent);
    margin-left: 6px;
  }
  .sep { color: var(--accent); margin: 0 8px; }
  .rule {
    height: 2px;
    background: var(--accent);
    margin: 8px 0 12px;
  }
  .details {
    font-size: 17px;
    color: var(--text);
    white-space: nowrap;
  }
  .details .label { color: var(--accent); font-weight: 700; }
</style>
</head>
<body>
<main class="stage">
  <section class="card card--front">
    <p class="brand">Quarry Vale</p>
    <ul class="services services--main">
      <li>Rope Access</li>
      <li>Confined Space</li>
      <li>Fall Arrest / Abseil Anchors</li>
    </ul>
    <ul class="services services--extra">
      <li>Safety Systems</li>
      <li>Rigging</li>
    </ul>
    <p class="site">www.<span class="domain">quarryvale</span>.co.nz</p>
  </section>

  <section class="card card--back">
    <p class="brand">Quarry Vale</p>
    <div class="contact-block">
      <div class="person">Reggie Stanton<span class="sep">\</span><span class="role">Director</span></div>
      <div class="rule"></div>
      <div class="details">
        <span class="label">T :</span> 027 816 4920<span class="sep">\</span>
        <span class="label">E :</span> reggie@quarryvale.co.nz<span class="sep">\</span>
        <span class="label">W :</span> www.quarryvale.co.nz
      </div>
    </div>
  </section>
</main>
</body>
</html>
```